We TEND toward Wedlock Event

I need a flyer to promote an Event we do that promotes Marriage and asks people to get involved in Ministry to Marriage. I need a graphic with the words: "We TEND toward Wedlock!"

Target Market(s)

Potential volunteers to get involve in the marriage ministry in a particular Catholic Parish.

Industry/Entity Type

Ministry

Logo Text

We TEND toward Wedlock!

Colors

Designer to choose colors to be used in the design.

Requirements
Must have
• Under the graphic should be the words: "An Event to Encourage and Support Marriages in our Parish"
• There could be a picture or pictures of married couples at different ages/stages.
• Other words include:
• "Please join us as we discuss the realities facing married couples today and what our response as a Parish can and should be."
• I also need a place to put name of Parish, date, time and location. This information will change for each event so the actual information will need to be left blank.
Nice to have
• Please make it eye-catching and something that would like to attend.
• WE hope the logo itself is fun and colorful.
• Would also like our non-profit logo along with the words "Conducted By..."(HearthWeaving USA) somewhere on flyer.

```html
<!DOCTYPE html>
<html lang="en">
<head>
<meta charset="utf-8">
<title>We Tend toward Wedlock – Event Flyer</title>
<link href="https://fonts.googleapis.com/css2?family=Great+Vibes&family=Didact+Gothic&display=swap" rel="stylesheet">
<style>
  :root {
    --paper: #ffffff;
    --paper-tint: #f7f5f6;
    --teal: #4d8a8d;
    --teal-dark: #24494b;
    --pink: #e4578b;
    --pink-soft: #f3a6c2;
    --magenta: #c8236a;
    --ink: #3a3a3a;
    --rule: #c9c9c9;
    --box-line: #e2e2e2;
  }
  * { margin: 0; padding: 0; box-sizing: border-box; }
  html, body { width: 678px; height: 1200px; overflow: hidden; background: var(--paper); }
  .flyer {
    position: relative;
    width: 678px;
    height: 1200px;
    background: radial-gradient(ellipse at 50% 55%, var(--paper) 0%, var(--paper-tint) 100%);
    font-family: "Didact Gothic", "Helvetica Neue", sans-serif;
    color: var(--ink);
    overflow: hidden;
  }
  .flowers { position: absolute; }
  .flowers--top-left { left: 0; top: 0; width: 200px; height: 300px; }
  .flowers--bottom-right { right: 0; bottom: 0; width: 190px; height: 420px; }

  .tagline {
    position: absolute; top: 32px; left: 402px;
    font-size: 10px; font-style: italic; font-weight: bold; color: var(--ink);
  }
  .org-mark {
    position: absolute; top: 62px; left: 236px;
    display: flex; align-items: center; gap: 10px;
  }
  .org-mark__square { width: 30px; height: 30px; background: var(--teal-dark); }
  .org-mark__name { font-size: 25px; color: var(--teal-dark); letter-spacing: 0.5px; }
  .org-site {
    position: absolute; top: 120px; left: 398px;
    font-size: 8px; color: var(--teal); font-weight: bold;
  }

  .collage { position: absolute; left: 66px; top: 145px; width: 546px; height: 560px; }

  .headline {
    position: absolute; left: 28px; right: 28px; top: 660px; height: 95px;
    font-family: "Great Vibes", cursive;
    border-bottom: 1px solid var(--teal);
  }
  .headline__lead { position: absolute; left: 0; top: 0; font-size: 66px; color: var(--teal); }
  .headline__tail { position: absolute; right: 0; top: 8px; font-size: 60px; color: var(--pink); }

  .event-title { position: absolute; left: 0; right: 0; top: 808px; text-align: center; }
  .event-title__lead { font-size: 26px; color: var(--teal); }
  .event-title__main { font-size: 32px; color: var(--pink); margin-top: 8px; letter-spacing: 0.5px; }
  .event-rule { position: absolute; left: 138px; right: 110px; top: 910px; border-top: 1px solid var(--rule); }
  .invite {
    position: absolute; left: 110px; right: 90px; top: 924px;
    text-align: center; font-size: 14px; line-height: 20px; color: var(--ink);
  }

  .details-box {
    position: absolute; left: 130px; top: 1010px; width: 330px; height: 165px;
    background: var(--paper);
    border: 1px solid var(--box-line);
    border-radius: 4px;
    box-shadow: 0 2px 4px rgba(0,0,0,0.08);
  }
  .locate-tag { position: absolute; left: 0; top: 1090px; width: 120px; height: 30px; }
  .locate-tag__label {
    position: absolute; left: 22px; top: 1096px;
    font-size: 16px; color: var(--paper);
  }
  .credit { position: absolute; left: 11px; top: 1140px; font-size: 11px; line-height: 15px; }
  .credit__lead { color: var(--teal); }
  .credit__org { color: var(--pink); }
</style>
</head>
<body>
<main class="flyer">
  <svg class="flowers flowers--top-left" viewBox="0 0 200 300" role="img" aria-label="Pink dahlias and roses with green stems in the top-left corner">
    <defs>
      <radialGradient id="bloomTop" cx="35%" cy="20%" r="80%">
        <stop offset="0%" stop-color="#f7a8c4"/>
        <stop offset="55%" stop-color="#e4578b"/>
        <stop offset="100%" stop-color="#e4578b" stop-opacity="0"/>
      </radialGradient>
    </defs>
    <path d="M0 0 H200 C170 60 120 70 90 120 C60 170 40 230 0 300 Z" fill="url(#bloomTop)"/>
  </svg>

  <svg class="flowers flowers--bottom-right" viewBox="0 0 190 420" role="img" aria-label="Pink dahlias and red roses climbing the bottom-right corner">
    <defs>
      <radialGradient id="bloomBottom" cx="75%" cy="85%" r="85%">
        <stop offset="0%" stop-color="#e4578b"/>
        <stop offset="50%" stop-color="#f3a6c2"/>
        <stop offset="100%" stop-color="#f3a6c2" stop-opacity="0"/>
      </radialGradient>
    </defs>
    <path d="M190 0 V420 H0 C60 400 90 360 120 300 C150 230 150 120 190 0 Z" fill="url(#bloomBottom)"/>
  </svg>

  <p class="tagline">"..Rebuild My Church!"</p>
  <div class="org-mark">
    <span class="org-mark__square"></span>
    <span class="org-mark__name">HearthWeaving USA</span>
  </div>
  <p class="org-site">www.hearthweavingusa.org</p>

  <svg class="collage" viewBox="0 0 546 560" role="img" aria-label="Heart-shaped collage of rounded wedding photos: rings, bouquets, joined hands, a bride and groom and a wedding cake topper">
    <defs>
      <linearGradient id="collageTone" x1="0" y1="0" x2="1" y2="1">
        <stop offset="0%" stop-color="#ece7e3"/>
        <stop offset="45%" stop-color="#d9c4bf"/>
        <stop offset="75%" stop-color="#e8b7c6"/>
        <stop offset="100%" stop-color="#dcd6d2"/>
      </linearGradient>
    </defs>
    <path d="M273 560 C210 490 20 360 10 210 C0 90 80 20 170 30 C230 36 262 80 273 120 C284 80 330 20 400 25 C490 30 546 100 540 200 C530 350 340 480 273 560 Z" fill="url(#collageTone)" stroke="#ffffff" stroke-width="6"/>
  </svg>

  <h1 class="headline">
    <span class="headline__lead">We Tend</span>
    <span class="headline__tail">toward Wedlock</span>
  </h1>

  <section class="event-title">
    <p class="event-title__lead">An Event to Encourage and Support</p>
    <p class="event-title__main">MARRIAGES IN OUR PARISH</p>
  </section>
  <div class="event-rule"></div>
  <p class="invite">Please join us as we discuss the realities facing married couples today and what our response as a Parish can and should be.</p>

  <div class="details-box" aria-label="Space for parish name, date, time and location"></div>

  <svg class="locate-tag" viewBox="0 0 120 30" aria-hidden="true">
    <polygon points="0,0 120,0 108,15 120,30 0,30" fill="var(--pink)"/>
  </svg>
  <p class="locate-tag__label">Locate Us:</p>

  <p class="credit">
    <span class="credit__lead">Conducted By...</span><br>
    <span class="credit__org">HearthWeaving USA</span>
  </p>
</main>
</body>
</html>
```